Neue Marke für Herrenaccessoires benötigt Flyer-Design
Zielgruppe
Wir sind ein junges Unternehmen die eine neue Marke für Herrenaccessoires aufbaut. KORVALO ist unsere neue Marke für hochwertige, stylishe Herrenaccessoires. Entstanden ist die Idee bie der Suche nach dem kompletten Look für den modernen Gentleman. Warum darf es bei den Herrenaccessoires nicht etwas mutiger zugehen in Sachen Farben und Mustern und das mit dem Anspruch hoher Materialqualität und Verarbeitung? Wo findet man komplette Accessoires-Angebote, bei denen man Krawatten, Einstecktücher, Socken, Gürtel und sogar Taschen in einem Shop farblich aufeinander abgestimmt finden kann? Diese Fragen haben wir uns gestellt und geben mit KORVALO unsere Antwort darauf. Mit KORVALO finden unsere Kunden sowohl für ihren Business- als auch für ihren Freizeitlook in Farbe und Styles perfekt kombinierbare Accessoires, die wir in von uns persönlich ausgewählten Manufakturen in Italien und der Türkei mit Sorgfalt und Know-how fertigen lassen.
Vom kontrastreichen, mutigen trendy Muster- und Farbmix zur klassischen Kombination Ton in Ton mit aktuellen Farben.
Unsere Zielgruppen sind mode- und stilbewusste Herren im Alter von 30 - 50.
Aufgabenstellung
Das Design sollte sich an unserem Web-Shop www.korvalo-shop.example orientieren.
Die Market KORVALO clean, minimalistisch und edel wahrgenommen werden.
Wir möchten die erste Marketingkampage mit einem Flyer starten. Die Flyer werden über eine Textilreinigungsfirma an die Reinigungsbügel (bei Hemden) befestigt. Aus diesem Grund sollte das Layout die Maße von ca. Breite: 9,5 cm x Höhe: 20 cm orientieren. Damit der Flyer (2seitig) auch an die Bügel umgehängt werden kann, muss oben auf dem Flyer ein Loch mit einem Durchmesser von 3 cm ein berücksichtigt werden.

```html
<!DOCTYPE html>
<html lang="de">
<head>
<meta charset="utf-8">
<title>KORVALO – Bügelanhänger</title>
<link href="https://fonts.googleapis.com/css2?family=Questrial&family=Montserrat:wght@700&display=swap" rel="stylesheet">
<style>
  :root {
    --page: #ffffff;
    --card: #ffffff;
    --ink: #1c1c1c;
    --hole-edge: #d2d2d2;
    --photo-light: #f2f2f2;
    --photo-mid: #cfcfcf;
    --socks-dark: #5c5853;
    --belts-dark: #3a2e2a;
    --ties-dark: #2a2a30;
    --scarves: #4a5a78;
    --social-square: #3b4a9a;
    --social-circle: #c8367a;
  }
  * { margin: 0; padding: 0; box-sizing: border-box; }
  html, body { width: 1200px; height: 1189px; overflow: hidden; background: var(--page); }
  body { position: relative; font-family: "Questrial", sans-serif; color: var(--ink); font-weight: 400; }
  h1, p { font-weight: 400; }

  .hanger { position: absolute; top: 241px; width: 339px; background: var(--card); overflow: hidden; border: 1px solid #ececec; }
  .hanger--front { left: 222px; height: 714px; }
  .hanger--back { left: 645px; height: 725px; }

  .hanger__hole { position: absolute; left: 116px; top: 17px; width: 106px; height: 106px; border-radius: 50%; background: var(--page); border: 2px solid var(--hole-edge); z-index: 3; }

  .hanger__backdrop { position: absolute; left: 0; top: 34px; width: 100%; height: 680px;
    background: radial-gradient(ellipse 50% 60% at 50% 45%, var(--photo-mid), var(--photo-light) 80%); z-index: 0; }

  .txt { position: absolute; left: 0; width: 100%; text-align: center; z-index: 2; }

  .front__headline { top: 236px; font-size: 43px; line-height: 45px; }
  .front__brand { top: 350px; font-size: 20px; letter-spacing: 3px; display: flex; align-items: center; justify-content: center; gap: 8px; }
  .front__brand-mark { width: 12px; height: 12px; background: var(--ink); }
  .front__invite { top: 427px; font-size: 21px; line-height: 25px; }
  .front__url { top: 454px; font-family: "Montserrat", sans-serif; font-weight: 700; font-size: 17px; }
  .front__strip { position: absolute; top: 497px; height: 63px; z-index: 2; }
  .front__strip--ties { left: 0; width: 162px; background: linear-gradient(90deg, #6f7a34, var(--ties-dark) 55%, #c9bfa8); }
  .front__strip--scarves { left: 176px; width: 163px; background: linear-gradient(90deg, #e9e4d8, var(--scarves) 55%, #7a3450); }
  .front__about { top: 579px; font-size: 21px; line-height: 25.6px; }

  .back__lead { top: 167px; font-size: 21px; line-height: 26px; }
  .back__offer { top: 220px; font-size: 44px; line-height: 50px; }
  .back__offer-note { top: 265px; font-size: 21px; }
  .back__photo { position: absolute; top: 321px; height: 174px; }
  .back__photo--socks { left: 0; width: 169px; background: linear-gradient(135deg, var(--socks-dark), #9a8a6e 50%, #556a3c); }
  .back__photo--belts { left: 183px; width: 156px; background: linear-gradient(160deg, #2e4a52, #5a3a6a 40%, var(--belts-dark)); }
  .back__code-label { top: 506px; font-size: 22px; }
  .back__code { top: 539px; font-size: 22px; }
  .back__social { position: absolute; top: 605px; left: 21px; right: 14px; display: flex; justify-content: space-between; font-size: 19px; z-index: 2; }
  .social { display: flex; align-items: center; gap: 8px; }
  .social__square { width: 26px; height: 26px; background: var(--social-square); border-radius: 3px; }
  .social__circle { width: 28px; height: 28px; background: var(--social-circle); border-radius: 50%; }
  .back__terms { top: 661px; font-size: 12px; line-height: 15px; }
</style>
</head>
<body>
  <section class="hanger hanger--front">
    <div class="hanger__backdrop" role="img" aria-label="Blasses Schwarzweißfoto eines Herrn im Anzug mit verschränkten Armen"></div>
    <div class="hanger__hole"></div>
    <h1 class="txt front__headline">Lust auf einen<br>neuen Style?</h1>
    <div class="txt front__brand"><span class="front__brand-mark"></span>KORVALO</div>
    <p class="txt front__invite">Lass Dich inspirieren:</p>
    <p class="txt front__url">www.korvalo-shop.example</p>
    <div class="front__strip front__strip--ties" role="img" aria-label="Foto von Krawatte und Einstecktuch am Sakko"></div>
    <div class="front__strip front__strip--scarves" role="img" aria-label="Foto gemusterter Einstecktücher"></div>
    <p class="txt front__about">Der neue Online-Shop mit<br>hochwertigen, stylishen<br>Herrenaccessoiren für den<br>modernen Gentleman.</p>
  </section>

  <section class="hanger hanger--back">
    <div class="hanger__hole"></div>
    <p class="txt back__lead">Löse den Rabattcode ein<br>und erhalte</p>
    <p class="txt back__offer">20 % Rabatt</p>
    <p class="txt back__offer-note">auf unsere Artikel!</p>
    <div class="back__photo back__photo--socks" role="img" aria-label="Foto farbiger Socken in Reihen"></div>
    <div class="back__photo back__photo--belts" role="img" aria-label="Foto aufgerollter Wildledergürtel"></div>
    <p class="txt back__code-label">Ihr Rabattcode*:</p>
    <p class="txt back__code">Kalvenxxx</p>
    <div class="back__social">
      <span class="social"><span class="social__square"></span>KORVALO</span>
      <span class="social"><span class="social__circle"></span>korvalo-official</span>
    </div>
    <p class="txt back__terms">*Gültig bis zum xx.xx.xxxx,<br>nicht kombinierbar mit anderen Rabattaktionen.</p>
  </section>
</body>
</html>
```